Willow Creek Wellness Academy (Massage School) Flyer Advertisment

We are a massage therapy/holistic healing school, operating in Los Angeles for over 16 years. We need a flyer/advertisement with the aim of attracting new students and potential future massage therapists. Our vision is a 4x6 (read vertical) flyer (potentially dual sided, due to amount of copy we have). The key aesthetic terms for this project are modern, feminine, minimal, natural, fun. The design should be eye catching yet feel organic (we want an advertisement, but keep in mind we are a holistic health institution.) We would like the primary color scheme to be focused around purple and white (green or beige are secondary), and would very much like to see the use of a literal Lavender plant (or multiple) included creatively. You do not need to use all the files we provided. Mandatory is the inclusion of ALL the copy provided in the word document attached, arranged at your discretion, as well as the logo file. We have also provided a picture of our school as well as a few massage photos to possibly be used (only if applicable). Please feel free to be creative with the exact font choices and exact color choices (we only selected the options here as reference.) Thank you all so much for your time and we look forward to reviewing the designs. *Note* we have selected a 5 day duration due to urgency but may be willing to extend for the right designer (please reach out to us if need be)

Target Market(s)

Potential students to become massage therapists or holistic health professionals

Industry/Entity Type

Education

Font styles to use
Sans Serif
Script

Colors
6b449b
ffffff
fbc994
9bcb3c

Requirements
Must have
• Use of Copy attached. Use of logo. use of Lavender plant
Nice to have
• Photo our school (included). Photos of massages being done on clients (examples included)
• * Would be great if you could allow room for rounded corners on the print job* not necessary

```html
<!DOCTYPE html>
<html lang="en">
<head>
<meta charset="utf-8">
<title>Willow Creek Wellness Academy – Become a Certified Massage Therapist</title>
<link rel="stylesheet" href="https://fonts.googleapis.com/css2?family=Montserrat:wght@400;600;700;800;900&family=Raleway:wght@400;500&display=swap">
<style>
  :root {
    --purple-deep: #6b449b;
    --purple-mid: #8e5fb0;
    --purple-top: #b08ac7;
    --lilac: #d6bfe2;
    --lilac-pale: #e6d8ee;
    --white: #ffffff;
    --lavender-a: #5b3a9e;
    --lavender-b: #7e62c0;
    --lavender-green: #7d9a5c;
    --skin-a: #e9c6ad;
    --skin-b: #c89379;
    --amber-a: #f0a13c;
    --amber-b: #9c3c0c;
    --school-a: #8a857d;
    --school-b: #4d4a44;
    --school-green: #6f8a4e;
    --text-dark: #3f3447;
  }
  * { margin: 0; padding: 0; box-sizing: border-box; }
  html, body { width: 801px; height: 1200px; overflow: hidden; }
  body { font-family: "Montserrat", sans-serif; background: var(--white); }

  .flyer {
    position: relative; width: 801px; height: 1200px; overflow: hidden;
    background: linear-gradient(180deg, var(--lilac) 0%, var(--lilac-pale) 55%, #efe6f3 100%);
  }
  .top-band {
    position: absolute; left: 0; top: 0; width: 801px; height: 138px;
    background: linear-gradient(180deg, var(--purple-mid) 0%, var(--purple-top) 100%);
  }
  .lavender-field {
    position: absolute; left: 0; top: 136px; width: 801px; height: 196px;
    background: linear-gradient(180deg, var(--lavender-b) 0%, var(--lavender-a) 45%, var(--lavender-green) 100%);
  }
  .brand-seal {
    position: absolute; left: 302px; top: 38px; width: 196px; height: 196px;
    border-radius: 50%; background: var(--white);
    box-shadow: 0 3px 10px rgba(60,30,90,.35);
    display: flex; align-items: center; justify-content: center; text-align: center;
  }
  .brand-name {
    font-family: "Montserrat", sans-serif; font-weight: 700; font-size: 19px;
    line-height: 1.2; color: var(--purple-deep); width: 150px;
  }

  .headline { position: absolute; left: 0; top: 350px; width: 801px; }
  .headline text { fill: var(--white); font-family: "Montserrat", sans-serif; }
  .headline .kicker { font-weight: 800; font-size: 38px; letter-spacing: 16px; }
  .headline .big { font-weight: 900; font-size: 132px; }
  .headline .sub { font-weight: 800; font-size: 62px; }

  .courses-title {
    position: absolute; left: 40px; top: 610px;
    font-weight: 700; font-size: 25px; color: var(--purple-deep);
  }
  .course-list { position: absolute; list-style: none; top: 651px; }
  .course-list.left { left: 40px; }
  .course-list.right { left: 270px; }
  .course-list li {
    position: relative; padding-left: 27px; margin-bottom: 7.3px;
    font-family: "Raleway", sans-serif; font-weight: 500; font-size: 18.5px;
    line-height: 21.5px; color: var(--text-dark);
  }
  .course-list li svg { position: absolute; left: 0; top: 4px; width: 17px; height: 15px; }

  .photo {
    position: absolute; left: 460px; width: 300px; height: 128px;
    border: 2px solid var(--white); box-shadow: 0 3px 8px rgba(0,0,0,.3);
  }
  .photo.back-massage { top: 614px; background: linear-gradient(120deg, #f6efe9 0%, var(--skin-a) 35%, var(--skin-b) 100%); }
  .photo.face-massage { top: 766px; background: linear-gradient(120deg, var(--amber-b) 0%, var(--amber-a) 50%, #f3c06a 100%); }

  .school-photo {
    position: absolute; left: 0; top: 905px; width: 801px; height: 295px;
    background:
      linear-gradient(90deg, rgba(111,138,78,0) 0%, rgba(111,138,78,0) 60%, rgba(111,138,78,.75) 100%),
      linear-gradient(180deg, rgba(138,133,125,0) 0%, var(--school-a) 40%, var(--school-b) 100%);
  }
  .web-address {
    position: absolute; right: 41px; top: 1137px;
    font-weight: 700; font-size: 23px; letter-spacing: 2.5px; color: var(--white);
    text-shadow: 0 1px 4px rgba(0,0,0,.5);
  }
</style>
</head>
<body>
<main class="flyer">
  <div class="top-band"></div>
  <div class="lavender-field" role="img" aria-label="Photo of a blooming lavender field"></div>

  <div class="brand-seal">
    <span class="brand-name">Willow Creek Wellness Academy</span>
  </div>

  <svg class="headline" width="801" height="230" viewBox="0 0 801 230" aria-label="Become a certified massage therapist!">
    <text class="kicker" x="400" y="40" text-anchor="middle">BECOME A</text>
    <text class="big" x="40" y="158" textLength="720" lengthAdjust="spacingAndGlyphs">CERTIFIED</text>
    <text class="sub" x="40" y="222" textLength="720" lengthAdjust="spacingAndGlyphs">MASSAGE THERAPIST!</text>
  </svg>

  <h2 class="courses-title">WCWA offers courses in:</h2>

  <ul class="course-list left">
    <li><svg viewBox="0 0 17 15"><path d="M1 8 L6 13 L16 1" fill="none" stroke="#6b449b" stroke-width="3" stroke-linecap="round" stroke-linejoin="round"/></svg>Swedish</li>
    <li><svg viewBox="0 0 17 15"><path d="M1 8 L6 13 L16 1" fill="none" stroke="#6b449b" stroke-width="3" stroke-linecap="round" stroke-linejoin="round"/></svg>Deep Tissue</li>
    <li><svg viewBox="0 0 17 15"><path d="M1 8 L6 13 L16 1" fill="none" stroke="#6b449b" stroke-width="3" stroke-linecap="round" stroke-linejoin="round"/></svg>Myofascial Release</li>
    <li><svg viewBox="0 0 17 15"><path d="M1 8 L6 13 L16 1" fill="none" stroke="#6b449b" stroke-width="3" stroke-linecap="round" stroke-linejoin="round"/></svg>Chair Massage</li>
    <li><svg viewBox="0 0 17 15"><path d="M1 8 L6 13 L16 1" fill="none" stroke="#6b449b" stroke-width="3" stroke-linecap="round" stroke-linejoin="round"/></svg>Aromatherapy</li>
    <li><svg viewBox="0 0 17 15"><path d="M1 8 L6 13 L16 1" fill="none" stroke="#6b449b" stroke-width="3" stroke-linecap="round" stroke-linejoin="round"/></svg>Energy Healing</li>
    <li><svg viewBox="0 0 17 15"><path d="M1 8 L6 13 L16 1" fill="none" stroke="#6b449b" stroke-width="3" stroke-linecap="round" stroke-linejoin="round"/></svg>Crystal &amp;<br>Gemstone Therapy</li>
    <li><svg viewBox="0 0 17 15"><path d="M1 8 L6 13 L16 1" fill="none" stroke="#6b449b" stroke-width="3" stroke-linecap="round" stroke-linejoin="round"/></svg>Shiatsu</li>
  </ul>

  <ul class="course-list right">
    <li><svg viewBox="0 0 17 15"><path d="M1 8 L6 13 L16 1" fill="none" stroke="#6b449b" stroke-width="3" stroke-linecap="round" stroke-linejoin="round"/></svg>Lymphatic</li>
    <li><svg viewBox="0 0 17 15"><path d="M1 8 L6 13 L16 1" fill="none" stroke="#6b449b" stroke-width="3" stroke-linecap="round" stroke-linejoin="round"/></svg>Sports Massage</li>
    <li><svg viewBox="0 0 17 15"><path d="M1 8 L6 13 L16 1" fill="none" stroke="#6b449b" stroke-width="3" stroke-linecap="round" stroke-linejoin="round"/></svg>Pregnancy<br>Massage</li>
    <li><svg viewBox="0 0 17 15"><path d="M1 8 L6 13 L16 1" fill="none" stroke="#6b449b" stroke-width="3" stroke-linecap="round" stroke-linejoin="round"/></svg>Hot Stone<br>Massage</li>
    <li><svg viewBox="0 0 17 15"><path d="M1 8 L6 13 L16 1" fill="none" stroke="#6b449b" stroke-width="3" stroke-linecap="round" stroke-linejoin="round"/></svg>Polarity Therapy<br>and more!</li>
  </ul>

  <div class="photo back-massage" role="img" aria-label="Photo of hands giving a back massage"></div>
  <div class="photo face-massage" role="img" aria-label="Photo of a relaxing facial massage in warm light"></div>

  <div class="school-photo" role="img" aria-label="Photo of the academy's building with trees"></div>
  <p class="web-address">www.gowcwa.org</p>
</main>
</body>
</html>
```